Top label sticker design -Australian Owned

We are seeking to develop a top sticker for our range of batteries, 80mm x 30mm.
Enclosed is the current top label sample, and new label will also be added. The message we want to send is, state that we are "100% Australian Family Owned", would like to use our Brindara Logo merged with an Australian flag or similar to show the strength and roots of our brand.

Target Market(s)

30 to 50 year old males

Industry/Entity Type

Automotive

Requirements
Must have
• "100% Australian Family Owned" text or similar wording
Brindara logo
Nice to have
• Blend of Australian flag with/ across our Brindara logo.
Red background colour, Kestrel Mail Red.
Should not have
• To much much fluff, want to achieve a short sharp message.

```html
<!DOCTYPE html>
<html lang="en">
<head>
<meta charset="utf-8">
<title>Brindara – 100% Australian Family Owned top label</title>
<link href="https://fonts.googleapis.com/css2?family=Montserrat:wght@600&family=Open+Sans:wght@500&display=swap" rel="stylesheet">
<style>
  :root {
    --page: #f4f4f4;
    --navy-deep: #001443;
    --navy-glow: #3658a6;
    --flag-red: #c8353a;
    --white: #ffffff;
  }
  html, body {
    margin: 0;
    width: 1200px;
    height: 698px;
    overflow: hidden;
    background: var(--page);
  }
  .stage {
    position: relative;
    width: 1200px;
    height: 698px;
  }
  .top-label {
    position: absolute;
    left: 40px;
    top: 139px;
    width: 1120px;
    height: 420px;
    display: block;
  }
  .ownership-line {
    font-family: "Montserrat", sans-serif;
    font-weight: 600;
    font-size: 64px;
    fill: var(--white);
  }
  .badge-figure {
    font-family: "Montserrat", sans-serif;
    font-weight: 600;
    font-size: 30px;
    fill: var(--flag-red);
  }
  .brand-name {
    font-family: "Open Sans", sans-serif;
    font-weight: 500;
    font-size: 176px;
    fill: var(--white);
  }
  .product-range {
    font-family: "Open Sans", sans-serif;
    font-weight: 500;
    font-size: 52px;
    fill: var(--white);
  }
</style>
</head>
<body>
<main class="stage">
  <svg class="top-label" viewBox="0 0 1617 606" xmlns="http://www.w3.org/2000/svg" aria-label="Brindara top label: 100% Australian Family Owned">
    <defs>
      <radialGradient id="label-glow" cx="1104" cy="238" r="760" gradientUnits="userSpaceOnUse" gradientTransform="translate(1104 238) scale(1 0.6) translate(-1104 -238)">
        <stop offset="0" stop-color="var(--navy-glow)"/>
        <stop offset="1" stop-color="var(--navy-deep)"/>
      </radialGradient>
      <linearGradient id="red-wash" x1="0" y1="0" x2="0.55" y2="0.75">
        <stop offset="0" stop-color="var(--flag-red)"/>
        <stop offset="0.38" stop-color="var(--flag-red)" stop-opacity="0.85"/>
        <stop offset="1" stop-color="var(--flag-red)" stop-opacity="0"/>
      </linearGradient>
    </defs>

    <g class="flag-artwork" role="img" aria-label="Artwork area: Australian flag inspired red bands and Southern Cross stars over navy">
      <rect width="1617" height="606" fill="url(#label-glow)"/>
      <rect width="1617" height="606" fill="url(#red-wash)"/>
    </g>

    <g class="ownership">
      <circle cx="92" cy="57" r="47" fill="var(--white)"/>
      <text class="badge-figure" x="92" y="68" text-anchor="middle" transform="rotate(-18 92 57)">100%</text>
      <text class="ownership-line" x="154" y="81">Australian Family Owned</text>
    </g>

    <g class="brand">
      <text class="brand-name" x="697" y="288" textLength="742" lengthAdjust="spacingAndGlyphs">Brindara</text>
      <text class="product-range" x="699" y="358" textLength="737" lengthAdjust="spacingAndGlyphs">BATTERIES  OILS  FILTERS</text>
    </g>
  </svg>
</main>
</body>
</html>
```